Tarnovel canola oil needs a lable design

We need to design a label for our TARNOVEL brand canola oil. We want our product to be easily noticed on supermarket shelves and clearly identified as Australian-made, distinguishing it from other canola oils. Our product is 100% Australian-made, non-GMO canola oil. The packaging size is 2 liters. The front and back label designs are required.
Updates

The label needs to be advanced, high-class and eye-catching. The Logo is just a reference and can be redesigned if there is a better idea.

I invited a new designer to create a design on Monday, but I haven't received the design work yet. I'm worried that my time might have expired and that he wasn't able to upload it.

Target Market(s)

high-end supermarket

Industry/Entity Type

cold pressed canola oil

Requirements
Must have
• 100% Australian-made,non-GMO,nutrition board,Kosher certification,Halal certification,HACCP
Nice to have
• easily be noticed at supermarket and clearly identified as Australian-made;different from the existing canola oil label design

```html
<!DOCTYPE html>
<html lang="en">
<head>
<meta charset="utf-8">
<title>Tarnovel Canola Oil – Front Label</title>
<link href="https://fonts.googleapis.com/css2?family=Caprasimo&family=Cherry+Swash:wght@700&family=Poppins:wght@400;500&family=Oswald:wght@600&display=swap" rel="stylesheet">
<style>
  :root {
    --page: #f4f4f2;
    --sun-light: #fff6a8;
    --sun: #fbe54a;
    --sun-deep: #f2cf1c;
    --leaf-light: #a9d35a;
    --leaf: #6fae1f;
    --leaf-dark: #4e7a12;
    --olive-ink: #3f4d12;
    --mist: #e6e6e4;
    --ink: #2d2d2d;
    --cream: #fff8c8;
  }
  * { margin: 0; padding: 0; box-sizing: border-box; }
  html, body { width: 1200px; height: 800px; overflow: hidden; background: var(--page); }
  .canvas { position: relative; width: 1200px; height: 800px; }

  .label {
    position: absolute; left: 413px; top: 40px; width: 375px; height: 720px;
    overflow: hidden;
    background: radial-gradient(circle at 55% 48%, var(--sun-light) 0%, var(--sun) 45%, var(--sun-deep) 100%);
  }

  .flowers-top {
    position: absolute; left: 0; top: 0; width: 375px; height: 170px;
    background: linear-gradient(180deg, rgba(242,207,28,0.55) 0%, rgba(251,229,74,0) 100%);
  }
  .flowers-cluster {
    position: absolute; left: 271px; top: 414px; width: 104px; height: 203px;
    border-radius: 50px 0 0 50px;
    background: radial-gradient(ellipse at 55% 45%, #f5d21e 0%, #e8c31a 55%, rgba(150,170,60,0.6) 100%);
  }

  .gmo-seal {
    position: absolute; left: 271px; top: 21px; width: 82px; height: 82px; border-radius: 50%;
    background: var(--leaf-dark); border: 5px solid #d9b64a;
  }

  .map-shape {
    position: absolute; left: 28px; top: 222px; width: 305px; height: 245px;
    border-radius: 46% 54% 42% 58% / 40% 38% 62% 60%;
    background: radial-gradient(ellipse at 50% 45%, var(--leaf-light) 0%, #b8db6e 70%, rgba(184,219,110,0.6) 100%);
  }

  .brand {
    position: absolute; left: 104px; top: 272px;
    font-family: "Cherry Swash", serif; font-weight: 700; font-size: 31px;
    color: var(--olive-ink);
  }
  .product {
    position: absolute; left: 38px; top: 296px;
    font-family: "Caprasimo", serif; font-size: 76px; line-height: 1;
    color: var(--cream);
    -webkit-text-stroke: 3px var(--olive-ink);
    paint-order: stroke fill;
    text-shadow: 2px 3px 0 var(--leaf-dark);
  }
  .product-kind {
    position: absolute; left: 228px; top: 368px;
    font-family: "Caprasimo", serif; font-size: 60px; line-height: 1;
    color: var(--cream);
    -webkit-text-stroke: 3px var(--olive-ink);
    paint-order: stroke fill;
    text-shadow: 2px 3px 0 var(--leaf-dark);
  }
  .claim-figure {
    position: absolute; left: 60px; top: 432px;
    font-family: "Caprasimo", serif; font-size: 48px; line-height: 1;
    color: #d4ec8e;
    -webkit-text-stroke: 2px var(--leaf-dark);
    paint-order: stroke fill;
  }
  .claim-text {
    position: absolute; left: 60px; top: 484px;
    font-family: "Poppins", sans-serif; font-weight: 500; font-size: 19px; letter-spacing: -0.5px;
    color: #c6e477;
    -webkit-text-stroke: 1px var(--leaf-dark);
    paint-order: stroke fill;
  }

  .footer-band { position: absolute; left: 0; top: 0; width: 375px; height: 720px; }

  .use {
    position: absolute; width: 80px; text-align: center;
    font-family: "Poppins", sans-serif; font-size: 11.5px; color: var(--ink);
  }
  .use-icon {
    display: block; width: 66px; height: 66px; margin: 0 auto 6px;
    border-radius: 50%; background: var(--leaf); border: 3px solid #ffffff;
    box-shadow: 0 0 0 1px #c9c9c9;
  }
  .use-icon svg { width: 60px; height: 60px; }
  .use--cooking { left: 9px; top: 510px; }
  .use--frying { left: 87px; top: 542px; }
  .use--roasting { left: 171px; top: 564px; }

  .origin-badge {
    position: absolute; left: 16px; top: 658px; width: 162px; height: 42px;
    border: 2px solid #1f7a4a; border-radius: 3px; background: #ffffff;
  }
  .volume {
    position: absolute; left: 239px; top: 661px;
    font-family: "Oswald", sans-serif; font-weight: 600; font-size: 33px; letter-spacing: 0.5px;
    color: var(--olive-ink);
  }
</style>
</head>
<body>
<main class="canvas">
  <section class="label">
    <div class="flowers-top" role="img" aria-label="Yellow canola blossoms and green leaves scattered across the top"></div>

    <div class="gmo-seal" role="img" aria-label="Non-GMO seal"></div>

    <div class="map-shape" role="img" aria-label="Light green map of Australia behind the product name"></div>

    <svg class="footer-band" viewBox="0 0 375 720" aria-hidden="true">
      <path d="M0 443 C 40 530, 150 600, 375 625 L375 720 L0 720 Z" fill="var(--leaf)"/>
      <path d="M0 452 C 40 536, 150 604, 375 631 L375 720 L0 720 Z" fill="var(--mist)"/>
    </svg>

    <div class="flowers-cluster" role="img" aria-label="Cluster of canola flowers on a stem"></div>

    <div class="brand">Tarnovel</div>
    <div class="product">Canola</div>
    <div class="product-kind">oil</div>
    <div class="claim-figure">100%</div>
    <div class="claim-text">AUSTRALIAN MADE</div>

    <div class="use use--cooking">
      <span class="use-icon">
        <svg viewBox="0 0 60 60" aria-hidden="true">
          <rect x="18" y="27" width="24" height="14" rx="3" fill="#fff"/>
          <rect x="15" y="24" width="30" height="4" rx="2" fill="#fff"/>
          <rect x="12" y="30" width="5" height="3" rx="1.5" fill="#fff"/>
          <rect x="43" y="30" width="5" height="3" rx="1.5" fill="#fff"/>
          <path d="M25 20 q2 -3 0 -6 M30 20 q2 -3 0 -6 M35 20 q2 -3 0 -6" stroke="#fff" stroke-width="1.5" fill="none"/>
        </svg>
      </span>
      COOKING
    </div>
    <div class="use use--frying">
      <span class="use-icon">
        <svg viewBox="0 0 60 60" aria-hidden="true">
          <circle cx="33" cy="26" r="9" fill="#fff"/>
          <path d="M27 31 L19 39" stroke="#fff" stroke-width="4" stroke-linecap="round"/>
          <circle cx="17" cy="41" r="2.5" fill="#fff"/>
        </svg>
      </span>
      FRYING
    </div>
    <div class="use use--roasting">
      <span class="use-icon">
        <svg viewBox="0 0 60 60" aria-hidden="true">
          <ellipse cx="30" cy="30" rx="12" ry="8" fill="#fff"/>
          <rect x="14" y="38" width="32" height="3" rx="1.5" fill="#fff"/>
        </svg>
      </span>
      ROASTING
    </div>

    <div class="origin-badge" role="img" aria-label="Country of origin badge"></div>
    <div class="volume">2 LITRES</div>
  </section>
</main>
</body>
</html>
```